Ward Compass Business Card Design*

We need a business card design for our company Ward Compass. Our company is specialized in providing online consulting services regarding medical institutions, hospitals and doctors. We work with patients worldwide looking to choose between healthcare providers. We have a website you may use as a reference, where we list doctors and clinics worldwide. So we target Medical providers as well as patients worldwide.
Target Market(s)
Medical Providers and patients around the world
Industry/Entity Type
Medical
Contact Information for Business Card
Salma Derkaoui
CEO
+90 612 348 2071
info@wardcompass-example.com
www.wardcompass-example.com
14 Annakhil 3 H.R.B. Rabat, Morocco
Requirements
Must have
- Company logo/name on one full side, personal info and smaller logo and company name on the other side.
Nice to have
- Smart and elegant design

```html
<!DOCTYPE html>
<html lang="en">
<head>
<meta charset="utf-8">
<title>Ward Compass Business Card</title>
<link rel="stylesheet" href="https://fonts.googleapis.com/css2?family=Montserrat:wght@400;600;700&display=swap">
<style>
  :root {
    --backdrop: #e6e4e0;
    --card-white: #f7f7f7;
    --navy: #1f4a85;
    --navy-deep: #1b3f73;
    --grey: #6f7378;
    --grey-light: #b9bcc0;
    --rule: #c9cbce;
    --white: #ffffff;
  }
  * { margin: 0; padding: 0; box-sizing: border-box; }
  html, body { width: 900px; height: 1200px; overflow: hidden; }
  body {
    background: var(--backdrop);
    font-family: "Montserrat", Arial, sans-serif;
    position: relative;
  }
  .card {
    position: absolute;
    left: 90px;
    width: 720px;
    height: 410px;
    box-shadow: 0 6px 18px rgba(0,0,0,0.18);
  }
  .card--front { top: 150px; background: var(--card-white); }
  .card--back { top: 640px; background: var(--navy); }

  .brand {
    position: absolute;
    display: flex;
    align-items: center;
    left: 50%;
    transform: translateX(-50%);
    white-space: nowrap;
  }
  .brand__dot { border-radius: 50%; flex: none; }
  .brand__name { font-weight: 700; letter-spacing: 0.01em; }

  .card--front .brand { top: 48px; }
  .card--front .brand__dot { width: 40px; height: 40px; background: var(--navy); margin-right: 12px; }
  .card--front .brand__name { font-size: 26px; color: var(--navy-deep); }

  .holder { position: absolute; top: 150px; left: 0; right: 0; text-align: center; }
  .holder__name { font-size: 22px; color: var(--grey); letter-spacing: 0.02em; }
  .holder__name strong { color: var(--navy); font-weight: 700; }
  .holder__role { font-size: 13px; color: var(--grey); margin-top: 2px; }

  .contact {
    position: absolute;
    top: 212px;
    left: 258px;
    width: 210px;
    list-style: none;
    font-size: 12.5px;
    color: var(--grey);
  }
  .contact__item {
    display: flex;
    align-items: center;
    height: 30px;
    border-top: 1px solid var(--rule);
  }
  .contact__item:last-child { border-bottom: 1px solid var(--rule); }
  .contact__icon { width: 16px; height: 16px; margin-right: 10px; flex: none; }
  .contact__address {
    height: auto;
    padding: 8px 0;
    line-height: 1.45;
    display: block;
  }

  .card--back .brand { top: 150px; }
  .card--back .brand__dot { width: 86px; height: 86px; background: var(--white); margin-right: 18px; }
  .card--back .brand__name { font-size: 46px; color: var(--white); }

  .website {
    position: absolute;
    bottom: 34px;
    left: 0; right: 0;
    text-align: center;
    font-size: 13px;
    letter-spacing: 0.14em;
    color: var(--white);
  }
</style>
</head>
<body>
  <section class="card card--front">
    <div class="brand">
      <span class="brand__dot"></span>
      <span class="brand__name">WARD COMPASS</span>
    </div>
    <div class="holder">
      <p class="holder__name"><strong>SALMA</strong> DERKAOUI</p>
      <p class="holder__role">CEO</p>
    </div>
    <ul class="contact">
      <li class="contact__item">
        <svg class="contact__icon" viewBox="0 0 16 16" aria-hidden="true">
          <circle cx="8" cy="8" r="8" fill="#1f4a85"/>
          <path d="M5.3 4.2l1.3 1.6-.8.9c.5 1.1 1.3 1.9 2.4 2.4l.9-.8 1.6 1.3-.8 1.3c-2.8-.3-5-2.5-5.3-5.3z" fill="#fff"/>
        </svg>
        +90 612 348 2071
      </li>
      <li class="contact__item">
        <svg class="contact__icon" viewBox="0 0 16 16" aria-hidden="true">
          <circle cx="8" cy="8" r="8" fill="#1f4a85"/>
          <rect x="4" y="5.2" width="8" height="5.6" fill="#fff"/>
          <path d="M4 5.2l4 3 4-3" fill="none" stroke="#1f4a85" stroke-width="0.9"/>
        </svg>
        info@wardcompass-example.com
      </li>
      <li class="contact__item contact__address">
        14 Annakhil 3 H.R.B.<br>Rabat, Morocco
      </li>
    </ul>
  </section>

  <section class="card card--back">
    <div class="brand">
      <span class="brand__dot"></span>
      <span class="brand__name">WARD COMPASS</span>
    </div>
    <p class="website">www.wardcompass-example.com</p>
  </section>
</body>
</html>
```